eCommerce website for a DIY shop & communal center

We need a website for a business called The Maker Loft. The Maker Loft is both a shop and communal establishment where people with shared interests, especially in DIY (Do It Yourself) and crafting, can gather to shop for & work on projects while sharing ideas, equipment, supplies and knowledge. The shop is both brick & motor and online. The physical communal space provides workstations, equipment, tools and supplies and expertise for DIY lovers to create their projects.

Target Market(s)

Middle & upper class DIY enthusiasts, creative hobbyists, budding artists & small business owners

Industry/Entity Type

DIY, Arts & Crafts

Coding

Coded - Design and coding required

Number of Pages Required

5+ page

Requirements
Must have
• Menus to include 1. home page (with about us, operating hours, contacts, location, meet the team); 2. Studio activities (how to DIY at the Studio, booking, equipment & tools, house rules); 3. Studio events (events in the Studio, offsite events); 4. Resources (FAQs, tutorials, blogs, eBooks) and 5. Online shop
Nice to have
• Branding guidelines eg logo colours (see attachment) to influence design. Woo commerce shop. Booking feature for activities & events at the Studio.

```html
<!DOCTYPE html>
<html lang="en">
<head>
<meta charset="utf-8">
<title>The Maker Loft — Studio Events</title>
<link href="https://fonts.googleapis.com/css2?family=Roboto:wght@400;500;700;900&family=Satisfy&display=swap" rel="stylesheet">
<style>
:root{
  --orange:#f47b20;
  --blue:#2a93d5;
  --ink:#1f1f1f;
  --muted:#6b6b6b;
  --line:#e6e6e6;
  --footer:#111111;
  --footer-text:#bdbdbd;
  --white:#ffffff;
  --bg:#ffffff;
}
*{margin:0;padding:0;box-sizing:border-box}
html,body{width:1200px;height:2216px;overflow:hidden;background:var(--bg)}
body{font-family:"Roboto",Arial,sans-serif;color:var(--ink);position:relative}

/* header */
.topbar{height:40px;display:flex;align-items:center;justify-content:space-between;padding:0 100px;font-size:13px;color:var(--ink)}
.topbar .phone{display:flex;align-items:center;gap:8px}
.socials{display:flex;gap:8px}
.socials span{width:22px;height:22px;border-radius:50%;border:1px solid #cfcfcf;display:block}
.navbar{height:48px;border-top:1px solid var(--line);display:flex;align-items:center;padding:0 40px;position:relative}
.nav-group{display:flex;gap:34px;font-size:13px;font-weight:500;text-transform:uppercase;flex:1}
.nav-group.right{justify-content:flex-end}
.nav-group .active{color:var(--orange)}
.brand{position:absolute;left:50%;top:-40px;transform:translateX(-50%);width:180px;height:124px;background:var(--white);border-radius:0 0 10px 10px;box-shadow:0 3px 10px rgba(0,0,0,.12);display:flex;flex-direction:column;align-items:center;justify-content:center;gap:8px;z-index:3}
.brand .mark{width:18px;height:18px;border-radius:50%;background:var(--orange)}
.brand .name{font-weight:900;font-size:20px;color:var(--orange)}

.hero{height:304px;background:linear-gradient(100deg,#3a2f27 0%,#7a6a5c 45%,#b8aa98 70%,#5b4d42 100%);position:relative}
.hero h1{position:absolute;left:100px;top:108px;color:var(--white);font-weight:900;font-size:40px;letter-spacing:.5px;text-transform:uppercase}

/* events */
.events{padding:0 100px}
.section-title{font-family:"Satisfy",cursive;color:var(--orange);font-size:32px;text-align:center;margin-top:98px}
.section-title + .rule{width:60px;height:2px;background:var(--orange);margin:6px auto 14px}
.intro{width:520px;margin:0 auto;text-align:center;font-size:13px;line-height:20px;color:var(--muted)}
.grid{display:grid;grid-template-columns:repeat(3,1fr);gap:32px 24px;margin-top:64px}
.card{background:var(--white);box-shadow:0 4px 16px rgba(0,0,0,.12);height:480px}
.card .photo{height:220px;position:relative}
.p1{background:linear-gradient(135deg,#6e5a48,#b09a7f)}
.p2{background:linear-gradient(135deg,#4a4a52,#9a8e80)}
.p3{background:linear-gradient(135deg,#e3e0d8,#8c5c3a)}
.p4{background:linear-gradient(135deg,#3c4450,#a7a39a)}
.p5{background:linear-gradient(135deg,#2f3a52,#c9a78a)}
.p6{background:linear-gradient(135deg,#5a4a3c,#c8b39a)}
.date{position:absolute;left:12px;bottom:-12px;background:var(--blue);color:var(--white);font-size:11px;height:24px;display:flex;align-items:center;gap:12px;padding:0 10px}
.card .body{padding:28px 16px 0}
.card h3{font-size:19px;font-weight:700;margin-bottom:8px}
.card p{font-size:12.5px;line-height:18px;color:var(--muted)}
.card .obj{font-weight:700;color:var(--ink);margin-top:10px;font-size:13px}
.author{display:flex;align-items:center;gap:12px;border-top:1px solid var(--line);margin-top:14px;padding-top:14px}
.avatar{width:40px;height:40px;border-radius:50%;background:linear-gradient(135deg,#8a7462,#c9b8a6)}
.author b{display:block;font-size:13px}
.author small{font-size:11px;color:var(--muted)}

.actions{display:flex;justify-content:center;gap:60px;margin-top:88px}
.btn{width:180px;height:44px;border-radius:22px;color:var(--white);font-size:13px;font-weight:700;display:flex;align-items:center;justify-content:center;text-transform:uppercase}
.btn.orange{background:var(--orange)}
.btn.blue{background:var(--blue)}

/* footer */
.footer{position:absolute;left:0;top:1912px;width:1200px;height:304px;background:var(--footer);color:var(--footer-text)}
.cols{display:flex;padding:36px 100px 0;font-size:12.5px;line-height:21px}
.col h4{color:var(--white);font-size:14px;font-weight:700;margin-bottom:8px;text-transform:uppercase}
.c1{width:135px}.c2{width:185px}.c3{width:145px}.c4{width:235px}.c5{flex:1}
.email{height:36px;background:var(--white);border-radius:18px;color:#999;font-size:12px;display:flex;align-items:center;padding-left:16px;width:240px}
.subscribe{height:36px;width:240px;border-radius:18px;background:var(--orange);color:var(--white);font-weight:700;font-size:12px;display:flex;align-items:center;justify-content:center;margin-top:10px}
.f-socials{display:flex;gap:10px;justify-content:center;width:240px;margin-top:14px}
.f-socials span{width:28px;height:28px;border-radius:50%;background:var(--white);display:block}
.copyright{position:absolute;left:0;bottom:0;width:100%;height:40px;border-top:1px solid #2a2a2a;display:flex;align-items:center;justify-content:center;font-size:12px}
</style>
</head>
<body>
<header>
  <div class="topbar">
    <div class="phone">
      <svg width="14" height="14" viewBox="0 0 24 24"><path d="M6.6 10.8a15 15 0 0 0 6.6 6.6l2.2-2.2a1 1 0 0 1 1-.25 11.4 11.4 0 0 0 3.6.57 1 1 0 0 1 1 1V20a1 1 0 0 1-1 1A17 17 0 0 1 3 4a1 1 0 0 1 1-1h3.5a1 1 0 0 1 1 1c0 1.25.2 2.45.57 3.57a1 1 0 0 1-.25 1z" fill="#f47b20"/></svg>
      888 - 888 - 8888
    </div>
    <div class="socials"><span></span><span></span><span></span><span></span></div>
  </div>
  <nav class="navbar">
    <div class="nav-group"><span>Home</span><span>Studio Activities</span><span class="active">Studio Events</span></div>
    <div class="brand"><span class="mark"></span><span class="name">The Maker Loft</span></div>
    <div class="nav-group right"><span>Resources</span><span>Online Shop</span><span>Contact Us</span></div>
  </nav>
</header>

<section class="hero" role="img" aria-label="Workshop photo of a mitre saw on a workbench">
  <h1>Sudio Events</h1>
</section>

<main class="events">
  <h2 class="section-title">Offsite Events</h2>
  <div class="rule"></div>
  <p class="intro">Lorem ipsum dolor sit amet, consectetur adipiscing elit, sed do eiusmod tempor incididunt ut labore et dolore magna aliqua. Quis ipsum suspendisse ultrices gravida.</p>

  <div class="grid">
    <article class="card">
      <div class="photo p1" role="img" aria-label="Group of makers at an outdoor workshop"><span class="date"><span>04 OCT 2021</span><span>10 AM</span></span></div>
      <div class="body">
        <h3>Finibus Bonorum et Malorum</h3>
        <p>Lorem ipsum dolor sit, consectetur adipiscing elit sed do eiusmod tempor incididunt ut labore et dolore quis suspendisse ultrices gravida.</p>
        <p class="obj">Workshop Objectives:</p>
        <p>Finibus Bonorum et Malorum Sed ut perspicia</p>
        <div class="author"><span class="avatar"></span><div><b>John Smith</b><small>Finibus Bonorum et Malorum</small></div></div>
      </div>
    </article>
    <article class="card">
      <div class="photo p2" role="img" aria-label="Participants gathered around a project table"><span class="date"><span>04 OCT 2021</span><span>10 AM</span></span></div>
      <div class="body">
        <h3>Finibus Bonorum et Malorum</h3>
        <p>Lorem ipsum dolor sit, consectetur adipiscing elit sed do eiusmod tempor incididunt ut labore et dolore quis suspendisse ultrices gravida.</p>
        <p class="obj">Workshop Objectives:</p>
        <p>Finibus Bonorum et Malorum Sed ut perspicia</p>
        <div class="author"><span class="avatar"></span><div><b>John Smith</b><small>Finibus Bonorum et Malorum</small></div></div>
      </div>
    </article>
    <article class="card">
      <div class="photo p3" role="img" aria-label="Event poster for a weekend DIY workshop"><span class="date"><span>04 OCT 2021</span><span>10 AM</span></span></div>
      <div class="body">
        <h3>Finibus Bonorum et Malorum</h3>
        <p>Lorem ipsum dolor sit, consectetur adipiscing elit sed do eiusmod tempor incididunt ut labore et dolore quis suspendisse ultrices gravida.</p>
        <p class="obj">Workshop Objectives:</p>
        <p>Finibus Bonorum et Malorum Sed ut perspicia</p>
        <div class="author"><span class="avatar"></span><div><b>John Smith</b><small>Finibus Bonorum et Malorum</small></div></div>
      </div>
    </article>
    <article class="card">
      <div class="photo p4" role="img" aria-label="Team working together on a build"><span class="date"><span>04 OCT 2021</span><span>10 AM</span></span></div>
      <div class="body">
        <h3>Finibus Bonorum et Malorum</h3>
        <p>Lorem ipsum dolor sit, consectetur adipiscing elit sed do eiusmod tempor incididunt ut labore et dolore quis suspendisse ultrices gravida.</p>
        <p class="obj">Workshop Objectives:</p>
        <p>Finibus Bonorum et Malorum Sed ut perspicia</p>
        <div class="author"><span class="avatar"></span><div><b>John Smith</b><small>Finibus Bonorum et Malorum</small></div></div>
      </div>
    </article>
    <article class="card">
      <div class="photo p5" role="img" aria-label="Young makers painting at a craft table"><span class="date"><span>04 OCT 2021</span><span>10 AM</span></span></div>
      <div class="body">
        <h3>Finibus Bonorum et Malorum</h3>
        <p>Lorem ipsum dolor sit, consectetur adipiscing elit sed do eiusmod tempor incididunt ut labore et dolore quis suspendisse ultrices gravida.</p>
        <p class="obj">Workshop Objectives:</p>
        <p>Finibus Bonorum et Malorum Sed ut perspicia</p>
        <div class="author"><span class="avatar"></span><div><b>John Smith</b><small>Finibus Bonorum et Malorum</small></div></div>
      </div>
    </article>
    <article class="card">
      <div class="photo p6" role="img" aria-label="Maker using hand tools on wood"><span class="date"><span>04 OCT 2021</span><span>10 AM</span></span></div>
      <div class="body">
        <h3>Finibus Bonorum et Malorum</h3>
        <p>Lorem ipsum dolor sit, consectetur adipiscing elit sed do eiusmod tempor incididunt ut labore et dolore quis suspendisse ultrices gravida.</p>
        <p class="obj">Workshop Objectives:</p>
        <p>Finibus Bonorum et Malorum Sed ut perspicia</p>
        <div class="author"><span class="avatar"></span><div><b>John Smith</b><small>Finibus Bonorum et Malorum</small></div></div>
      </div>
    </article>
  </div>

  <div class="actions">
    <span class="btn orange">Past Events</span>
    <span class="btn blue">Your Events</span>
  </div>
</main>

<footer class="footer">
  <div class="cols">
    <div class="col c1"><h4>About</h4>Our Story<br>Press<br>Locations<br>Blog<br>Contact Us</div>
    <div class="col c2"><h4>Our Offering</h4>Projects<br>Paint Room<br>Parties<br>Classes</div>
    <div class="col c3"><h4>Other</h4>Franchise<br>Gift Cards<br>FAQ<br>Refund Policy</div>
    <div class="col c4"><h4>Contact Us</h4>1234 Somestreet Anywhere USA<br>21212<br>888-888-8888<br>hello@makerloft.example</div>
    <div class="col c5"><h4>Get Updates &amp; Promos</h4>
      <div class="email">Email Address</div>
      <div class="subscribe">SUBSCRIBE</div>
      <div class="f-socials"><span></span><span></span><span></span><span></span></div>
    </div>
  </div>
  <div class="copyright">Copyright © 2021 The Maker Loft. All rights reserved.</div>
</footer>
</body>
</html>
```